Business cards, letterheads, envelopes, notepad design

We are a new business in Miami, Florida. We produce business printing, signs and photogifts such as canvas prints, t shirts, mugs, phone cases etc.
Our store will be very modern with interactive stations for clients to design their own products on our cloud design software. We want something that will appeal to business clients and the general public clients.
We need designs for business cards, letterheads, notepads, and envelopes - all 4 colour process - full bleed OK.

Target Market(s)

We target both business clients and the general public.

Industry/Entity Type

Store

Font styles to use
Sans Serif
Other font styles liked:
• Harabara

Colors
acd036
33a6d7
e34197
000000

Requirements
Must have
• Cyan, Magenta, Lime Green
Should not have
• No cats. Absolutely.

```html
<!DOCTYPE html>
<html lang="en">
<head>
<meta charset="utf-8">
<title>Printvale Stationery</title>
<link href="https://fonts.googleapis.com/css2?family=Varela+Round&family=Montserrat:wght@400;500;700&display=swap" rel="stylesheet">
<style>
  :root{
    --stage:#e4e4e4;
    --paper:#ffffff;
    --ink:#1f1f1f;
    --charcoal:#3b3b3b;
    --footer:#555555;
    --magenta:#e34197;
    --cyan:#33a6d7;
    --lime:#acd036;
    --blue-top:#3b71ad;
    --blue-bottom:#29abe2;
    --flap:#ececec;
    --muted:#6a6a6a;
    --sign:#e6ebf8;
  }
  *{margin:0;padding:0;box-sizing:border-box}
  html,body{width:1200px;height:752px;overflow:hidden;background:var(--stage)}
  body{position:relative;font-family:"Montserrat",sans-serif;color:var(--ink)}
  .piece{position:absolute;background:var(--paper);overflow:hidden}
  .brand{font-family:"Varela Round",sans-serif;font-weight:400;color:var(--ink);position:absolute;white-space:nowrap;line-height:1}
  .brand--light{color:#fff}
  .deco{position:absolute;inset:0;width:100%;height:100%}
  .contact-bar{position:absolute;left:0;right:0;display:flex;align-items:center;gap:14px;padding:0 28px;font-size:5.5px;color:#fff}
  .contact-item{display:flex;align-items:center;gap:4px;line-height:1.2;flex:none;white-space:nowrap}
  .contact-item svg{width:7px;height:7px;fill:currentColor;flex:none}

  /* letterhead */
  .letterhead-stack{left:66px;top:56px;width:272px;height:390px;background:#f4f4f4}
  .letterhead{left:62px;top:52px;width:270px;height:382px}
  .letterhead .brand{right:16px;top:36px;font-size:12px}
  .letter-body{position:absolute;left:27px;top:71px;width:216px;font-size:5.2px;line-height:1.12;text-align:justify}
  .letter-body p{margin-bottom:5px}
  .signature{position:absolute;left:186px;top:257px;width:52px;height:18px;background:var(--sign);border-radius:2px}
  .signer{position:absolute;right:28px;top:277px;font-size:5.4px;text-align:right;line-height:1.35}
  .letterhead .contact-bar{bottom:0;height:21px;background:var(--footer)}

  /* folder */
  .folder{left:401px;top:55px;width:271px;height:388px;background:linear-gradient(180deg,var(--blue-top),var(--blue-bottom))}
  .folder-spine{position:absolute;right:0;top:0;width:10px;height:100%;background:#4a4a4a}
  .folder .brand--small{left:16px;top:32px;font-size:12px}
  .folder .brand--hero{left:58px;top:176px;font-size:30px}
  .folder .contact-bar{bottom:0;right:10px;height:22px;background:#454545;padding:0 0 0 30px;gap:14px;font-size:5px}

  /* large envelope */
  .envelope-large{left:736px;top:58px;width:274px;height:390px}
  .envelope-flap{position:absolute;left:0;top:0;width:100%;height:56px}
  .envelope-large .brand{left:10px;top:372px;font-size:10px}
  .envelope-large .contact-bar{bottom:8px;left:80px;padding:0;gap:10px;font-size:4.5px;color:var(--cyan)}

  /* DL envelopes */
  .envelope-front{left:67px;top:523px;width:293px;height:132px}
  .envelope-front .brand{left:14px;top:22px;font-size:11px}
  .envelope-line{position:absolute;left:92px;bottom:6px;font-size:5px;color:var(--ink);white-space:nowrap}
  .envelope-back{left:391px;top:523px;width:292px;height:132px}

  /* business cards */
  .card-front{left:812px;top:483px;width:153px;height:87px}
  .card-front .brand{left:16px;top:15px;font-size:9px}
  .card-name{position:absolute;left:99px;top:29px;font-size:7px;font-weight:700;line-height:1;background:var(--paper);padding:1px 2px;white-space:nowrap}
  .card-role{position:absolute;left:118px;top:39px;font-size:4px;color:var(--muted);background:var(--paper);padding:0 2px}
  .card-contacts{position:absolute;left:14px;top:47px;font-size:4px;line-height:1.4;color:var(--ink)}
  .card-contacts li{list-style:none;display:flex;gap:4px;align-items:flex-start;margin-bottom:2px;white-space:nowrap}
  .card-contacts .dot{width:4px;height:3px;margin-top:1px;flex:none}
  .card-back{left:812px;top:587px;width:153px;height:91px;background:var(--charcoal)}
  .card-back .brand{left:50px;top:42px;font-size:12px}
</style>
</head>
<body>

<!-- Letterhead -->
<div class="piece letterhead-stack"></div>
<section class="piece letterhead">
  <svg class="deco" viewBox="0 0 270 382" aria-hidden="true">
    <g opacity="0.22">
      <rect x="120" y="40" width="20" height="260" fill="var(--magenta)" transform="rotate(18 130 170)"/>
      <rect x="150" y="80" width="16" height="240" fill="var(--cyan)" transform="rotate(18 158 200)"/>
      <rect x="60" y="160" width="18" height="200" fill="var(--lime)" transform="rotate(18 69 260)"/>
    </g>
  </svg>
  <span class="brand">Printvale</span>
  <div class="letter-body">
    <p>Lorem Ipsum<br>Lorem Ipsum<br>Lorem Ipsum</p>
    <p>Lorem ipsum dolor sit amet, consectetur adipiscing elit. Donec at commodo dolor, in fermentum orci. Donec semper tristique justo, a rhoncus quam gravida sed. Pellentesque pretium erat vel ligula scelerisque dapibus. Phasellus non interdum urna, eget feugiat tellus. Vivamus bibendum sapien et sapien scelerisque, vitae egestas nisi egestas. Duis malesuada a nisi id sodales. Cras suscipit sem at felis rhoncus viverra nec quis mi. Fusce dapibus dolor ac cursus luctus. Suspendisse ullamcorper libero in dui ullamcorper tincidunt. Nam vel tincidunt tortor, eu tristique nisl. Nunc ut accumsan massa. Nulla viverra vel erat ac interdum. Integer lacinia semper tincidunt. Duis vestibulum eleifend diam, at ultrices est faucibus ac. Proin lorem mi, porta eget interdum vel, cursus eget ligula. Donec fermentum, tortor non laoreet egestas, nulla diam volutpat urna, et pretium dui nibh at tortor. Aenean elementum egestas eros id rutrum. Nullam in lorem a massa laoreet consectetur. Integer molestie massa vel nisi volutpat dictum in in turpis.</p>
    <p>Lorem ipsum dolor sit amet, consectetur adipiscing elit. Donec at commodo dolor, in fermentum orci. Donec semper tristique justo, a rhoncus quam gravida sed. Pellentesque pretium erat vel ligula scelerisque dapibus. Phasellus non interdum urna, eget feugiat tellus. Vivamus bibendum sapien et sapien scelerisque, vitae egestas nisi egestas. Duis malesuada a nisi id sodales. Cras suscipit sem at felis rhoncus viverra nec quis mi. Fusce dapibus dolor ac cursus luctus. Suspendisse ullamcorper libero in dui ullamcorper tincidunt. Nam vel tincidunt tortor, eu tristique nisl.</p>
  </div>
  <div class="signature" role="img" aria-label="Handwritten signature"></div>
  <div class="signer">Mark Ellery<br>Chief Executive Officer</div>
  <div class="contact-bar">
    <span class="contact-item"><svg viewBox="0 0 10 10"><path d="M2 1l2 2-1 1.5a6 6 0 0 0 2.5 2.5L7 6l2 2-1.5 1.5C4.5 9.5.5 5.5.5 2.5z"/></svg>305-555-0142</span>
    <span class="contact-item"><svg viewBox="0 0 10 10"><path d="M0 2h10v6H0zM0 2l5 3.5L10 2"/></svg>hello@printvale.com</span>
    <span class="contact-item"><svg viewBox="0 0 10 10"><path d="M5 .5L10 5H8.5v4.5h-2.5V7H4v2.5H1.5V5H0z"/></svg>120 Harbor Lane<br>Bayside, Place 0210</span>
  </div>
</section>

<!-- Presentation folder -->
<section class="piece folder">
  <svg class="deco" viewBox="0 0 271 388" aria-hidden="true">
    <g fill="#fff" opacity="0.14">
      <rect x="120" y="60" width="16" height="220" transform="rotate(18 128 170)"/>
      <rect x="40" y="150" width="14" height="200" transform="rotate(18 47 250)"/>
    </g>
  </svg>
  <span class="brand brand--light brand--small">Printvale</span>
  <span class="brand brand--light brand--hero">Printvale</span>
  <div class="folder-spine"></div>
  <div class="contact-bar">
    <span class="contact-item"><svg viewBox="0 0 10 10"><path d="M2 1l2 2-1 1.5a6 6 0 0 0 2.5 2.5L7 6l2 2-1.5 1.5C4.5 9.5.5 5.5.5 2.5z"/></svg>305-555-0142</span>
    <span class="contact-item"><svg viewBox="0 0 10 10"><path d="M0 2h10v6H0zM0 2l5 3.5L10 2"/></svg>hello@printvale.com</span>
    <span class="contact-item"><svg viewBox="0 0 10 10"><path d="M5 .5L10 5H8.5v4.5h-2.5V7H4v2.5H1.5V5H0z"/></svg>120 Harbor Lane<br>Bayside, Place 0210</span>
  </div>
</section>

<!-- Large envelope -->
<section class="piece envelope-large">
  <svg class="envelope-flap" viewBox="0 0 274 56" preserveAspectRatio="none" aria-hidden="true">
    <path d="M0 0H274L248 56H26z" fill="var(--flap)"/>
  </svg>
  <svg class="deco" viewBox="0 0 274 390" aria-hidden="true">
    <rect x="150" y="160" width="14" height="190" fill="var(--magenta)" transform="rotate(12 157 255)"/>
    <rect x="110" y="210" width="13" height="140" fill="var(--cyan)" transform="rotate(12 116 280)"/>
    <rect x="40" y="250" width="13" height="140" fill="var(--lime)" transform="rotate(12 46 320)"/>
  </svg>
  <span class="brand">Printvale</span>
  <div class="contact-bar">
    <span class="contact-item"><svg viewBox="0 0 10 10"><path d="M2 1l2 2-1 1.5a6 6 0 0 0 2.5 2.5L7 6l2 2-1.5 1.5C4.5 9.5.5 5.5.5 2.5z"/></svg>305-555-0142</span>
    <span class="contact-item"><svg viewBox="0 0 10 10"><path d="M0 2h10v6H0zM0 2l5 3.5L10 2"/></svg>hello@printvale.com</span>
    <span class="contact-item"><svg viewBox="0 0 10 10"><path d="M5 .5L10 5H8.5v4.5h-2.5V7H4v2.5H1.5V5H0z"/></svg>120 Harbor Lane<br>Bayside, Place 0210</span>
  </div>
</section>

<!-- DL envelope, front -->
<section class="piece envelope-front">
  <svg class="deco" viewBox="0 0 293 132" aria-hidden="true">
    <rect x="240" y="0" width="11" height="132" fill="var(--magenta)" transform="rotate(14 245 66)"/>
    <rect x="215" y="30" width="10" height="110" fill="var(--cyan)" transform="rotate(14 220 85)"/>
    <rect x="185" y="50" width="10" height="100" fill="var(--lime)" transform="rotate(14 190 100)"/>
  </svg>
  <span class="brand">Printvale</span>
  <span class="envelope-line">lorem ipsumlorem ipsumlorem ipsumlorem ipsumlorem ipsumlorem ipsum</span>
</section>

<!-- DL envelope, back -->
<section class="piece envelope-back">
  <svg class="deco" viewBox="0 0 292 132" aria-hidden="true">
    <path d="M0 0H292L266 54H26z" fill="var(--charcoal)"/>
  </svg>
</section>

<!-- Business card, front -->
<section class="piece card-front">
  <svg class="deco" viewBox="0 0 153 87" aria-hidden="true">
    <rect x="124" y="5" width="7" height="80" fill="var(--magenta)" transform="rotate(14 127 45)"/>
    <rect x="110" y="25" width="6" height="66" fill="var(--cyan)" transform="rotate(14 113 58)"/>
    <rect x="92" y="40" width="6" height="56" fill="var(--lime)" transform="rotate(14 95 68)"/>
  </svg>
  <span class="brand">Printvale</span>
  <span class="card-name">ANA REYES</span>
  <span class="card-role">CEO</span>
  <ul class="card-contacts">
    <li><span class="dot" style="background:var(--magenta)"></span>305-555-0142</li>
    <li><span class="dot" style="background:var(--cyan)"></span>hello@printvale.com</li>
    <li><span class="dot" style="background:var(--lime)"></span>120 Harbor Lane<br>Bayside, Place 0210</li>
  </ul>
</section>

<!-- Business card, back -->
<section class="piece card-back">
  <svg class="deco" viewBox="0 0 153 91" aria-hidden="true">
    <g fill="#fff" opacity="0.08">
      <rect x="120" y="10" width="7" height="80" transform="rotate(14 123 50)"/>
      <rect x="100" y="30" width="6" height="66" transform="rotate(14 103 63)"/>
    </g>
  </svg>
  <span class="brand brand--light">Printvale</span>
</section>

</body>
</html>
```